Corvane Link Marketing Website

Corvane Link is the brand for a series of nation-wide internet peering exchanges operated by the Tallowmere Network Society Inc. (TNSI), a not-for-profit association founded in 1995.

Our current website is built on Drupal, and we are looking to migrate to WordPress with a similarly clean and modern theme:

http://www.corvanelink.example/

Target Market(s)

Technical and professional staff from the telecommunications industry in Australia.

Industry/Entity Type

Telecom

Font styles to use
Sans Serif

Requirements
Must have
• Responsive layout for mobile viewers
• Compatible with WordPress 4.2.2 and PHP 5.5.
• Winning entry will provide a completed WordPress theme file compatible .
• Usage of the "Corvane Link" logo must comply with the attached style guide.

```html
<!DOCTYPE html>
<html lang="en">
<head>
<meta charset="utf-8">
<title>Corvane Link – Internet Peering</title>
<link rel="stylesheet" href="https://fonts.googleapis.com/css2?family=Raleway:wght@300;400;500;600;700&display=swap">
<style>
:root{
  --gold:#e2b53b;
  --gold-dark:#c99d27;
  --blue:#3f74b8;
  --ink:#333333;
  --muted:#555555;
  --light:#f4f4f4;
  --white:#ffffff;
  --navy:#1d3f73;
}
*{box-sizing:border-box;margin:0;padding:0}
html,body{width:1200px;height:2624px;overflow:hidden}
body{font-family:"Raleway",sans-serif;color:var(--ink);background:var(--white);position:relative}
.abs{position:absolute}

/* header */
.site-header{position:absolute;left:0;top:0;width:1200px;height:105px;background:var(--white)}
.brand{position:absolute;left:93px;top:38px;display:flex;align-items:center;gap:12px}
.brand-mark{width:26px;height:26px;background:var(--gold)}
.brand-name{font-size:26px;font-weight:600;color:var(--navy);letter-spacing:.5px}
.main-nav{position:absolute;top:0;left:0;height:105px;width:1200px}
.main-nav a{position:absolute;top:48px;font-size:16px;color:var(--ink);text-decoration:none}
.main-nav a.active{color:var(--blue)}
.nav-underline{position:absolute;left:627px;top:100px;width:76px;height:4px;background:var(--gold)}

/* hero */
.hero{position:absolute;left:0;top:105px;width:1200px;height:490px;
  background:linear-gradient(110deg,#1a2c55 0%,#2463a8 30%,#3a8fd8 55%,#1c5aa0 75%,#0f2d5c 100%)}
.hero-cables{position:absolute;left:180px;top:0;width:420px;height:490px;
  background:linear-gradient(160deg,rgba(240,200,40,.0) 0%,rgba(240,200,40,.55) 45%,rgba(240,200,40,.15) 100%)}
.hero-caption{position:absolute;left:115px;top:175px;width:380px;height:171px;background:rgba(20,35,70,.72);padding:33px 26px}
.hero-caption h2{font-size:24px;font-weight:700;color:var(--gold);margin-bottom:6px}
.hero-caption p{font-size:15px;line-height:24px;color:var(--white)}
.hero-dots{position:absolute;left:566px;top:452px;display:flex;gap:8px}
.hero-dots span{width:8px;height:8px;border-radius:50%;background:var(--white)}
.hero-dots span.on{background:var(--gold)}

/* section headings */
.section-title{position:absolute;left:0;width:1200px;text-align:center;font-size:20px;font-weight:600;letter-spacing:.5px;color:var(--ink)}

/* what we do */
.feature{position:absolute;top:754px;width:320px}
.feature-img{width:320px;height:187px}
.feature h3{margin-top:35px;font-size:22px;font-weight:400;color:var(--blue)}
.feature p{margin-top:20px;font-size:13.5px;line-height:26px;color:var(--muted);height:110px}
.btn{display:inline-block;background:var(--gold);color:var(--white);font-size:15px;font-weight:600;padding:6px 16px;text-decoration:none}
.feature .btn{margin-top:12px}

/* about band */
.about-band{position:absolute;left:0;top:1278px;width:1200px;height:459px;
  background:linear-gradient(90deg,#5a6a80 0%,#7a8899 40%,#9aa3ae 100%)}
.about-panel{position:absolute;left:192px;top:0;width:424px;height:459px;background:rgba(40,80,150,.85);padding:110px 26px 0 28px}
.about-panel p{font-size:21px;line-height:30px;color:var(--white);font-weight:400}
.about-panel .btn{margin-top:24px;font-size:15px}
.about-photo{position:absolute;left:616px;top:0;width:584px;height:459px;
  background:linear-gradient(135deg,#8c8276 0%,#b4a898 45%,#4e6688 100%)}

/* services */
.service{position:absolute;top:1889px;width:235px}
.service-head{display:flex;align-items:flex-start;gap:14px;height:66px}
.service-icon{flex:none;width:46px;height:46px;background:var(--gold);display:flex;align-items:center;justify-content:center}
.service h4{font-size:16px;font-weight:600;color:var(--blue);line-height:22px;margin-top:1px}
.service p{margin-top:16px;font-size:12.5px;line-height:21.5px;color:var(--muted)}

/* partners */
.partners{position:absolute;left:0;top:2169px;width:1200px;height:201px;background:var(--light)}
.partners h5{position:absolute;top:36px;width:1200px;text-align:center;font-size:15px;font-weight:600;letter-spacing:.5px;color:var(--ink)}
.partner{position:absolute;top:110px;font-size:27px;font-weight:600;color:#3a3a3a;white-space:nowrap}

/* contact */
.contact{position:absolute;left:0;top:2370px;width:1200px;height:154px;background:var(--gold)}
.contact h5{position:absolute;top:25px;width:1200px;text-align:center;font-size:15px;font-weight:600;color:var(--white);letter-spacing:.5px}
.contact-item{position:absolute;display:flex;align-items:center;gap:16px;color:var(--white);font-size:15px;line-height:22px}
.follow{position:absolute;left:972px;top:69px;display:flex;align-items:center;gap:10px;color:var(--white);font-size:13px}
.follow span.dot{width:14px;height:14px;border-radius:50%;background:var(--white)}

/* footer */
.site-footer{position:absolute;left:0;top:2524px;width:1200px;height:100px;background:var(--white)}
.site-footer .brand{left:96px;top:33px}
.footer-nav{position:absolute;right:92px;top:27px;display:flex;gap:16px;font-size:14px;color:var(--ink)}
.footer-nav .sep{color:#777}
.copyright{position:absolute;right:92px;top:60px;font-size:13px;color:var(--ink)}
</style>
</head>
<body>

<header class="site-header">
  <div class="brand"><span class="brand-mark"></span><span class="brand-name">Corvane Link</span></div>
  <nav class="main-nav">
    <a class="active" style="left:647px">Home</a>
    <a style="left:738px">Services</a>
    <a style="left:847px">Organisation</a>
    <a style="left:985px">Blog</a>
    <a style="left:1079px">Contact</a>
    <span class="nav-underline"></span>
  </nav>
</header>

<section class="hero">
  <div class="hero-cables" role="img" aria-label="Photo of yellow fibre cables plugged into blue network switches"></div>
  <div class="hero-caption">
    <h2>Carrier neutral</h2>
    <p>Corvane Link is commercially neutral, carrier and ISP independent and is a not-for-profit organisation.</p>
  </div>
  <div class="hero-dots"><span class="on"></span><span></span><span></span><span></span></div>
</section>

<h2 class="section-title" style="top:684px">WHAT WE DO ?</h2>

<article class="feature" style="left:93px">
  <div class="feature-img" role="img" aria-label="Photo of a hand touching a network of connected member icons" style="background:linear-gradient(135deg,#a7adba 0%,#dfe2e8 50%,#8d95a6 100%)"></div>
  <h3>Member Owned</h3>
  <p>Corvane Link is owned and operated by the Tallowmere Network Society Inc., meaning we are owned and run by our members. To get involved please email</p>
  <a class="btn">Learn More</a>
</article>

<article class="feature" style="left:439px">
  <div class="feature-img" role="img" aria-label="Photo of blue patch cables in a network switch" style="background:linear-gradient(160deg,#5d8fd0 0%,#c9dcef 45%,#2f5fa8 100%)"></div>
  <h3>Commercially Neutral</h3>
  <p>Not only are we Carrier Neutral but here at Corvane Link we are also commercially neutral, this means anyone can peer provided you meet the technical requirements to do so.</p>
  <a class="btn">Learn More</a>
</article>

<article class="feature" style="left:785px">
  <div class="feature-img" role="img" aria-label="Map of Australia filled with the national flag" style="background:#ffffff;border:1px solid #dcdcdc;display:flex;align-items:center;justify-content:center">
    <div style="width:200px;height:120px;background:linear-gradient(135deg,#1f3f9a,#2c4fb5);border-radius:40% 50% 45% 55%"></div>
  </div>
  <h3>Australia Wide</h3>
  <p>At Corvane Link we are proud to operate 5 Peering Points throughout Australia. With a presence in 20 data centres across the nation we are bound to be at a data centre near you.</p>
  <a class="btn">Learn More</a>
</article>

<section class="about-band" role="img" aria-label="Photo of a glass-walled office interior">
  <div class="about-panel">
    <p>We are the country's only not-for-profit and independent internet peering provider. Member owned, carrier neutral,with proven high quality peering services since 1997.</p>
    <a class="btn">Learn More</a>
  </div>
  <div class="about-photo" role="img" aria-label="Photo of a smiling man in a checked shirt with arms crossed in an office"></div>
</section>

<h2 class="section-title" style="top:1810px">OUR SERVICES</h2>

<article class="service" style="left:94px">
  <div class="service-head">
    <span class="service-icon"><svg width="18" height="24" viewBox="0 0 18 24"><path d="M9 0C4 0 0 4 0 9c0 7 9 15 9 15s9-8 9-15c0-5-4-9-9-9z" fill="#fff"/><circle cx="9" cy="9" r="3.5" fill="#e2b53b"/></svg></span>
    <h4>Peering points across the nation</h4>
  </div>
  <p>At Corvane Link we have developed a robust peering fabric providing points of interconnect at most major data centres in Australia. This allows our members to participate in services, such as peering, where it is most beneficial for their network.</p>
</article>

<article class="service" style="left:352px">
  <div class="service-head">
    <span class="service-icon"><svg width="24" height="22" viewBox="0 0 24 22" fill="#fff"><rect x="9" y="0" width="6" height="6"/><rect x="0" y="16" width="6" height="6"/><rect x="9" y="16" width="6" height="6"/><rect x="18" y="16" width="6" height="6"/><path d="M11 6h2v4h9v6h-2v-4h-7v4h-2v-4H4v4H2v-6h9z"/></svg></span>
    <h4>Multilateral Peering Points</h4>
  </div>
  <p>Here at Corvane Link we operate an extensive multilateral peering network with points of presence in most states of Australia.</p>
</article>

<article class="service" style="left:612px">
  <div class="service-head">
    <span class="service-icon"><svg width="26" height="20" viewBox="0 0 26 20" fill="#fff"><circle cx="13" cy="5" r="4.5"/><path d="M4 20c0-6 4-9 9-9s9 3 9 9z"/><circle cx="4.5" cy="7" r="3"/><circle cx="21.5" cy="7" r="3"/><path d="M0 18c0-4 2-6 5-6 1 0 2 .3 2.5.7C5 14.5 4 16 4 18z"/><path d="M26 18c0-4-2-6-5-6-1 0-2 .3-2.5.7C21 14.5 22 16 22 18z"/></svg></span>
    <h4>Member Owned &amp; Driven</h4>
  </div>
  <p>Being member based our focus is always on offering the best level of service and benefits for members and not on profits; services offered and further developed take direction from member requirements.</p>
</article>

<article class="service" style="left:873px">
  <div class="service-head">
    <span class="service-icon"><svg width="22" height="20" viewBox="0 0 22 20" fill="none" stroke="#fff" stroke-width="2"><path d="M1 0v19h21"/><path d="M6 16V9M10 16V5M14 16V8M18 16V3" /></svg></span>
    <h4>Not-For-Profit</h4>
  </div>
  <p>Corvane Link is owned and operated by TNSI, a member based, not-for-profit association. All money is reinvested into services for members and stays within the association.</p>
</article>

<section class="partners">
  <h5>PEERING PARTNERS</h5>
  <span class="partner" style="left:132px">Northwind Cloud</span>
  <span class="partner" style="left:388px">Parcelo</span>
  <span class="partner" style="left:616px">Yondra</span>
  <span class="partner" style="left:812px">Kestrel CDN</span>
  <span class="partner" style="left:980px">Bayline</span>
</section>

<section class="contact">
  <h5>CONTACT US</h5>
  <div class="contact-item" style="left:112px;top:61px">
    <svg width="16" height="18" viewBox="0 0 16 18" fill="#fff"><path d="M2 0h14v14H4a2 2 0 0 0 0 4h12v-2H4V0z" opacity=".95"/></svg>
    <span>PO Box 4120, Perth Business Centre<br>Perth, WA 6849 AUSTRALIA</span>
  </div>
  <div class="contact-item" style="left:460px;top:69px">
    <svg width="16" height="16" viewBox="0 0 16 16" fill="#fff"><path d="M3 0l3 4-2 2c1 2.5 3.5 5 6 6l2-2 4 3-2 3C7 16 0 9 0 3z"/></svg>
    <span>1300 555 014</span>
  </div>
  <div class="contact-item" style="left:716px;top:69px">
    <svg width="20" height="15" viewBox="0 0 20 15"><rect width="20" height="15" fill="#fff"/><path d="M0 0l10 8 10-8" fill="none" stroke="#e2b53b" stroke-width="1.6"/></svg>
    <span>peering@corvanelink.example</span>
  </div>
  <div class="follow"><span>Follow Us</span><span class="dot"></span><span class="dot"></span></div>
</section>

<footer class="site-footer">
  <div class="brand"><span class="brand-mark"></span><span class="brand-name">Corvane Link</span></div>
  <nav class="footer-nav">
    <span>Home</span><span class="sep">|</span><span>Services</span><span class="sep">|</span><span>Organisation</span><span class="sep">|</span><span>Blog</span><span class="sep">|</span><span>Contact</span>
  </nav>
  <p class="copyright">© Copyright 2015 , All Rights Reserved</p>
</footer>

</body>
</html>
```